Metal head/ Sushi chef wanting artistic yet high imact business card

I'm sushi chef for make living in Australia originally from Tokyo Japan.
I'm also guitarist/composer as well on progressive metalcore/djent genre.
My favorite visual art is Mandala. Sacred geometries, Fractals, Paisleys are also things fit in me. I like dark color, earth color, and sometimes psychedelic patterns.
I want to hand out my business card when I meet new people in music industries or someone who is wanting private sushi chef for their party.
I know metal and sushi are far different subjects but they are all my passion. I would like to work with the designer who can create something cool from information above.

https://www.viewtrove.com/channel/QX7h4LpRzd2VnWe9kT3BFs8j
https://tunebarrel.com/user-817264093

Front
my name, Kenjiro Motsuba
occupation, "Sushi chef" "Metal guitarist/composer"
Email address, velmoquartz@mailorb.com
Phone number, (61)498271053

Back:
My Viewtrove channel, Pagefolk, Tunebarrel, Glintory. All of those are searchable by "Velmoquartz" The website mentioned above can be described as their logos.

Target Market(s)

people in Music industry, such as musicians, venue managers, promoters.
People who wants to have private sushi chef for their private function, party or events.

Industry/Entity Type

Artists

Contact Information for Business Card

Uploaded photos are just image reference. not thinking to use them.
My details:
I like :
energetic music that has a lot of details such as Progressive metalcore, jazz, djent, psychedelic music.
Spiritual thoughs, Buddism, fundamentals, relaxation music, 420, weed culture, Free thoughts
U.S street culture, skate board, kelps, surf, bicycle, nature, camping, hiking, ocean, mountain, desert, countryside,
permaculture, natural farming, organic farming, compost, self sufficient.
nigiri sushi, art sushi, something/someone beautiful in mind.

Dislike:
Fakes, Bullshits, format, negative, preservatives, artificial colors, illuminati, satanism, manipulation, mass favorites, big society, politics, Chinese letters on western design

Colors
0455a3
000000
7c7c7c
00a990
acd036
f37122

Requirements
Must have
• Front
• my name, Kenjiro Motsuba
• occupation, "Sushi chef" "Metal guitarist/composer"
• Email address, velmoquartz@mailorb.com
• Phone number, (61)498271053
• Back:
• My Viewtrove channel, Pagefolk, Tunebarrel, Glintory. All of those are searchable by "Velmoquartz" The website mentioned above can be described as their logos.
Nice to have
• something based on one of those either back ground or logo:
• Mandala, Sacred Geometry, Fractal art
Should not have
• pop essence. mass favorites, pink, Chinese letters, asian fonts, something asian

```html
<!DOCTYPE html>
<html lang="en">
<head>
<meta charset="utf-8">
<title>Kenjiro Motsuba – Business Card</title>
<link href="https://fonts.googleapis.com/css2?family=Lato:wght@400;700;900&display=swap" rel="stylesheet">
<style>
  :root {
    --stage: #2e2a28;
    --card: #ffffff;
    --pattern-light: #fbfbfb;
    --pattern-mid: #e6e6e6;
    --ink: #111111;
    --ink-soft: #2a2a2a;
    --photo-warm: #8a6a4c;
    --photo-dark: #3b2e24;
    --photo-light: #d9d2c6;
    --accent-orange: #f37122;
  }
  * { box-sizing: border-box; margin: 0; padding: 0; }
  html, body { width: 1200px; height: 844px; overflow: hidden; }
  body {
    background: var(--stage);
    font-family: "Lato", Arial, sans-serif;
    color: var(--ink);
    position: relative;
  }
  .card {
    position: absolute;
    top: 268px;
    width: 540px;
    height: 309px;
    background: var(--card);
    overflow: hidden;
  }
  .card--front { left: 40px; }
  .card--back { left: 620px; }
  .card__texture {
    position: absolute;
    inset: 0;
    background:
      radial-gradient(circle at 50% 45%, var(--pattern-light) 0%, #f1f1f1 55%, var(--pattern-mid) 100%);
  }
  .portrait {
    position: absolute;
    left: 34px;
    top: 112px;
    width: 226px;
    height: 172px;
    background: linear-gradient(135deg, var(--photo-dark) 0%, var(--photo-warm) 45%, var(--photo-light) 100%);
  }
  .details {
    position: absolute;
    left: 280px;
    top: 62px;
  }
  .details__name {
    font-size: 20px;
    font-weight: 900;
    text-transform: uppercase;
    letter-spacing: 0.2px;
    line-height: 1.1;
  }
  .details__roles {
    margin-top: 4px;
    font-size: 14px;
    font-weight: 700;
    line-height: 1.3;
  }
  .contact { margin-top: 14px; list-style: none; }
  .contact__item {
    display: flex;
    align-items: center;
    gap: 4px;
    font-size: 15px;
    font-weight: 700;
    line-height: 1.4;
  }
  .contact__icon { width: 14px; height: 14px; flex: none; }
  .social {
    margin-top: 22px;
    display: flex;
    align-items: center;
    gap: 5px;
    font-size: 12px;
    font-weight: 700;
  }
  .social__dot {
    width: 18px; height: 18px;
    border-radius: 50%;
    background: var(--ink);
    display: inline-block;
  }
  .social__handle { font-size: 16px; margin-left: 4px; }
  .channels {
    position: absolute;
    right: 24px;
    top: 148px;
  }
  .channels__labels {
    display: flex;
    justify-content: center;
    gap: 10px;
    font-size: 12px;
    font-weight: 700;
    color: var(--accent-orange);
    margin: 0 0 10px 90px;
  }
  .channels__link {
    display: block;
    font-size: 14px;
    font-weight: 400;
    color: var(--ink-soft);
    line-height: 1.5;
    text-align: right;
  }
</style>
</head>
<body>
  <section class="card card--front" aria-label="Business card front">
    <div class="card__texture" role="img" aria-label="Light grey sacred geometry line pattern background"></div>
    <div class="portrait" role="img" aria-label="Photo of the chef in kitchen whites holding a knife"></div>
    <div class="details">
      <h1 class="details__name">Kenjiro Motsuba</h1>
      <p class="details__roles">Sushi chef,<br>Metal guitarist/composer</p>
      <ul class="contact">
        <li class="contact__item">
          <svg class="contact__icon" viewBox="0 0 16 16" aria-hidden="true"><path d="M2 4c0-1 1-2 2-2h8c1 0 2 1 2 2v1h-3V4H5v1H2z M4 6h8l2 7H2z" fill="currentColor"/><circle cx="8" cy="10" r="1.8" fill="#fff"/></svg>
          (61)498271053
        </li>
        <li class="contact__item">
          <svg class="contact__icon" viewBox="0 0 16 16" aria-hidden="true"><rect x="1" y="3" width="14" height="10" fill="currentColor"/><path d="M1.5 3.5 8 9l6.5-5.5" fill="none" stroke="#fff" stroke-width="1.3"/></svg>
          velmoquartz@mailorb.com
        </li>
      </ul>
      <p class="social">
        <span class="social__dot"></span>Pagefolk
        <span class="social__dot"></span>Glintory
        <span class="social__handle">Velmoquartz</span>
      </p>
    </div>
  </section>

  <section class="card card--back" aria-label="Business card back">
    <div class="card__texture" role="img" aria-label="Light grey sacred geometry line pattern background"></div>
    <div class="channels">
      <p class="channels__labels"><span>Tunebarrel</span><span>Viewtrove</span></p>
      <span class="channels__link">www.tunebarrel.com/user-817264093</span>
      <span class="channels__link">www.viewtrove.com/channel/QX7h4LpRzd2VnWe9kT3BFs8j</span>
    </div>
  </section>
</body>
</html>
```